Chip Shop app

This task requires the creation of a number of images/icons for an example Zorvex app to demonstrate functionality in a forthcoming product.
The app will be called 'Velto' for a made up Fish n' Chip shop . The app will demonstrate the ability to request a delivery of food. The app will also provide prices and the ability to check on the current status of delivery. Icons will be needed (discussed below).
The following images are required:
A 90 x 90 pixel button (png and 180x180 retina versions too) for each of the following:
- A 'Menu' icon
- A 'Prices' icon
- A 'Order' icon
- Two 320 x 480 pixels background images (png and 640 x 960 retina version).
One of these images will be used for the 'Splash' image shown to a user when the app loads. The other background image will be used for the main app page where the buttons will be shown.
The 3 buttons will occupy the main page so the background of the main page should fit nicely with whatever position the 3 buttons will be placed in.
- An app icon (57 x 57 pixels and an identical 114 x 114 pixel for retina)
- A Melodrin connection image (512 x 512 pixels and a 1024 x 1024 identical version).
Since this is a made up company, the design is a 'blank canvas', so to speak. We're looking for something that looks beautiful and will do our app justice when put on display in the Quillbay.

```html
<!DOCTYPE html>
<html lang="en">
<head>
<meta charset="utf-8">
<title>Velto – Menu Screen</title>
<link rel="stylesheet" href="https://fonts.googleapis.com/css2?family=Open+Sans:wght@400&family=Roboto+Slab:wght@500;600&family=Roboto+Condensed:wght@400;500&display=swap">
<style>
:root{
  --stage:#1c1c1e;
  --panel-top:#b9b9bb;
  --panel-mid:#dcdcde;
  --panel-bottom:#c4c4c6;
  --ink:#3a3a3a;
  --icon-grey:#6b6b6b;
  --accent-red:#a34f4b;
  --tab-blue:#8aa3c8;
  --tab-blue-dark:#6f89b0;
  --tab-active:#c59592;
  --screen-cream:#efe8db;
  --card:#a87a73;
  --card-line:#6e4a45;
  --card-text:#fbefe6;
  --card-muted:#e3cfc8;
  --track:#241916;
}
*{box-sizing:border-box;margin:0;padding:0}
html,body{width:1200px;height:1000px;overflow:hidden}
body{position:relative;background:var(--stage);font-family:"Open Sans",sans-serif}

.intro-panel{position:absolute;left:0;top:0;width:595px;height:1000px;
  background:linear-gradient(180deg,var(--panel-top) 0%,var(--panel-mid) 55%,var(--panel-bottom) 100%);
  color:var(--ink);text-align:center}
.intro-title{position:absolute;top:112px;left:0;width:580px;font-size:60px;font-weight:400}
.intro-copy{position:absolute;top:246px;left:0;width:580px;font-size:39px;line-height:56px}
.intro-icons{position:absolute;top:558px;left:64px;width:460px;height:142px}
.intro-note{position:absolute;top:896px;left:0;width:575px;font-size:40px;color:var(--accent-red)}

.app-screen{position:absolute;left:636px;top:100px;width:530px;height:797px;background:var(--screen-cream)}
.tab-bar{display:flex;height:80px}
.tab{flex:1;background:linear-gradient(180deg,var(--tab-blue),var(--tab-blue-dark));border-right:2px solid #5d7396;
  display:flex;align-items:center;justify-content:center;position:relative}
.tab:last-child{border-right:none}
.tab.is-active{background:linear-gradient(180deg,#d3a6a2,var(--tab-active))}
.tab svg{width:52px;height:52px}
.cart-badge{position:absolute;right:0;top:0;width:0;height:0;border-top:30px solid #c9a3a6;border-left:30px solid transparent}
.cart-count{position:absolute;right:4px;top:2px;font-size:14px;color:#fff;font-family:"Roboto Condensed",sans-serif}

.menu-card{position:absolute;left:18px;top:103px;width:494px;height:672px;background:var(--card);border-radius:8px;
  box-shadow:0 2px 6px rgba(0,0,0,.25)}
.menu-pointer{position:absolute;left:250px;top:-14px;border-left:14px solid transparent;border-right:14px solid transparent;border-bottom:14px solid var(--card)}
.menu-title{position:absolute;left:200px;top:16px;font-family:"Roboto Condensed",sans-serif;font-size:32px;color:var(--card-muted);letter-spacing:1px}
.featured-num{position:absolute;left:40px;top:20px;font-family:"Roboto Condensed",sans-serif;font-size:32px;color:var(--card-muted)}
.featured-name{position:absolute;left:44px;top:64px;font-family:"Roboto Slab",serif;font-weight:500;font-size:18px;color:var(--card-text)}
.featured-desc{position:absolute;left:44px;top:113px;font-family:"Roboto Condensed",sans-serif;font-weight:500;font-size:16px;line-height:21px;color:#2e1d1a}
.order-action{position:absolute;left:206px;top:100px;width:50px;text-align:center;font-family:"Roboto Condensed",sans-serif;font-size:14px;color:#f3e6df}
.price-tag{position:absolute;left:302px;top:116px}
.featured-art{position:absolute;left:356px;top:44px;width:112px;height:124px;border-radius:50% 40% 45% 50%;
  background:linear-gradient(160deg,#e6d79a 0%,#9aa9d6 60%,#7f8fc4 100%)}

.menu-list{position:absolute;left:12px;top:205px;width:414px;list-style:none}
.menu-item{height:66.5px;border-top:1.5px solid var(--card-line);display:flex;align-items:center;position:relative}
.item-num{width:74px;padding-left:28px;font-family:"Roboto Condensed",sans-serif;font-size:32px;color:var(--card-muted)}
.item-name{font-family:"Roboto Slab",serif;font-weight:600;font-size:18px;color:var(--card-text)}
.item-more{position:absolute;left:306px;top:30px;font-size:20px;color:var(--card-text);letter-spacing:1px}

.scroll-track{position:absolute;left:448px;top:182px;width:18px;height:466px;background:var(--track);border-radius:9px;box-shadow:inset 0 1px 3px #000}
.scroll-thumb{position:absolute;left:3px;top:3px;width:12px;height:152px;border-radius:6px;background:linear-gradient(90deg,#8d7f7b,#c9bcb8,#8d7f7b)}
</style>
</head>
<body>

<section class="intro-panel">
  <h1 class="intro-title">Menu Screen</h1>
  <p class="intro-copy">customizable buttons,<br>colors, free positioning<br>panels (top or bottom),<br>scroll bars and boxes.</p>
  <svg class="intro-icons" viewBox="0 0 460 142" fill="var(--icon-grey)" aria-hidden="true">
    <!-- menu book -->
    <g transform="translate(4,0)">
      <path d="M0 6l16 0 6 28-16 2z"/>
      <ellipse cx="52" cy="20" rx="14" ry="18"/>
      <rect x="48" y="30" width="8" height="22"/>
      <path d="M86 4l4 2-12 34-4-2zM96 8l4 2-12 32-4-2zM104 14l4 2-12 28-4-2z"/>
      <path d="M0 44q28-8 54 6v86q-26-12-54-4zM108 44q-28-8-54 6v86q26-12 54-4z"/>
      <g fill="#cfcfcf"><rect x="8" y="62" width="38" height="3"/><rect x="8" y="74" width="38" height="3"/><rect x="8" y="86" width="38" height="3"/><rect x="8" y="98" width="38" height="3"/><rect x="62" y="62" width="38" height="3"/><rect x="62" y="74" width="20" height="3"/><rect x="86" y="74" width="14" height="18"/><rect x="62" y="98" width="38" height="3"/></g>
    </g>
    <!-- order tray -->
    <g transform="translate(170,0)">
      <path d="M0 70l18-16h20v14H22L14 76h32v12h34V76h32l-8-8H88V54h20l18 16v52a8 8 0 0 1-8 8H8a8 8 0 0 1-8-8z"/>
      <path d="M40 62l58-58 16 16-58 58-22 6z"/>
    </g>
    <!-- price tag -->
    <g transform="translate(330,10)">
      <path d="M70 0h50v50L54 116a8 8 0 0 1-11 0L4 78a8 8 0 0 1 0-11z"/>
      <circle cx="98" cy="24" r="9" fill="#d6d6d6"/>
      <text x="52" y="88" transform="rotate(-45 52 72)" font-family="Open Sans,sans-serif" font-size="44" fill="#d6d6d6" text-anchor="middle">$</text>
    </g>
  </svg>
  <p class="intro-note">3rd page of preview</p>
</section>

<main class="app-screen">
  <nav class="tab-bar">
    <div class="tab"><svg viewBox="0 0 52 52" fill="#fff"><path d="M26 8L4 28h6v16h12V32h8v12h12V28h6z"/></svg></div>
    <div class="tab"><svg viewBox="0 0 52 52" fill="#fff"><path d="M22 4h8l1 6 5 2 5-4 6 6-4 5 2 5 6 1v8l-6 1-2 5 4 5-6 6-5-4-5 2-1 6h-8l-1-6-5-2-5 4-6-6 4-5-2-5-6-1v-8l6-1 2-5-4-5 6-6 5 4 5-2z"/><circle cx="26" cy="26" r="8" fill="var(--tab-blue)"/></svg></div>
    <div class="tab is-active"><svg viewBox="0 0 52 52" fill="#fff"><path d="M6 4h6l3 14-7 1z"/><ellipse cx="26" cy="10" rx="6" ry="8"/><path d="M40 2l2 1-6 16-2-1zM45 5l2 1-6 15-2-1z"/><path d="M4 22q12-4 22 3v25q-10-6-22-2zM48 22q-12-4-22 3v25q10-6 22-2z"/><rect x="34" y="30" width="8" height="9" fill="var(--tab-active)"/></svg></div>
    <div class="tab"><svg viewBox="0 0 52 52" fill="none" stroke="#fff" stroke-width="5"><circle cx="22" cy="22" r="14"/><path d="M32 32l14 14" stroke-linecap="round" stroke-width="7"/></svg></div>
    <div class="tab"><svg viewBox="0 0 52 52" fill="none" stroke="#fff" stroke-width="4"><path d="M4 8h8l6 24h24l5-16H15"/><circle cx="21" cy="42" r="4" fill="#fff"/><circle cx="39" cy="42" r="4" fill="#fff"/></svg>
      <span class="cart-badge"></span><span class="cart-count">3</span></div>
  </nav>

  <section class="menu-card">
    <span class="menu-pointer"></span>
    <h2 class="menu-title">MENU</h2>
    <span class="featured-num">1</span>
    <h3 class="featured-name">Fish ‘n Velto</h3>
    <p class="featured-desc">Delicious CodFish<br>+ velto<br>+ sauce</p>
    <div class="order-action">
      <svg width="48" height="50" viewBox="0 0 48 50" fill="#f3e6df"><path d="M0 28l8-7h8v6H10l-3 3h14v5h14v-5h14l-3-3h-7v-6h8l8 7v20H0z"/><path d="M16 26l24-24 6 6-24 24-9 3z"/></svg>
      order
    </div>
    <svg class="price-tag" width="58" height="32" viewBox="0 0 58 32"><path d="M2 2h40l14 14-14 14H2z" fill="#efe4dc" stroke="#b89890"/><circle cx="44" cy="16" r="3" fill="#9a7a72"/><text x="8" y="22" font-family="Roboto Condensed,sans-serif" font-size="16" fill="#6a4c46">0 $</text></svg>
    <div class="featured-art" role="img" aria-label="Illustration of a blue fish holding a golden chip"></div>

    <ol class="menu-list">
      <li class="menu-item"><span class="item-num">2</span><span class="item-name">Fish ‘n Velto 2</span><span class="item-more">...</span></li>
      <li class="menu-item"><span class="item-num">3</span><span class="item-name">Fish ‘n Velto 3</span><span class="item-more">...</span></li>
      <li class="menu-item"><span class="item-num">4</span><span class="item-name">Fish ‘n Velto 4</span><span class="item-more">...</span></li>
      <li class="menu-item"><span class="item-num">5</span><span class="item-name">Fish ‘n Velto 5</span><span class="item-more">...</span></li>
      <li class="menu-item"><span class="item-num">6</span><span class="item-name">Fish ‘n Velto 6</span><span class="item-more">...</span></li>
      <li class="menu-item"><span class="item-num">7</span><span class="item-name">Fish ‘n Velto 7</span><span class="item-more">...</span></li>
      <li class="menu-item"><span class="item-num">8</span><span class="item-name">Fish ‘n Velto 8</span><span class="item-more">...</span></li>
    </ol>

    <div class="scroll-track"><span class="scroll-thumb"></span></div>
  </section>
</main>

</body>
</html>
```